Coralbend Pastoral Traders Business Cards

We require business cards revamped with our logo. A few details we would like to use.

1. Round Edges
2. Our logo over the top of a wagyu cattle background photo on one side of the card

Other side of the card has the below details.

1. Person Name (First & Last)
2. Job Position
3. Mobile Number
4. Email Address
5. Website Address

Simple & Neat.

Target Market(s)

Sales

Industry/Entity Type

Agriculture

Contact Information for Business Card

CORALBEND PASTORAL TRADERS

Colors

Designer to choose colors to be used in the design.

Requirements
Must have
• Company Logo

```html
<!DOCTYPE html>
<html lang="en">
<head>
<meta charset="UTF-8">
<title>Coralbend Pastoral Traders – Business Cards</title>
<link href="https://fonts.googleapis.com/css2?family=Montserrat:wght@400;500;700&display=swap" rel="stylesheet">
<style>
  :root {
    --backdrop: #2c2c2c;
    --card-white: #ffffff;
    --brand-maroon: #7a1c2c;
    --ink-dark: #3a2a2e;
    --ink-soft: #4a4a4a;
    --sky-top: #2f7fd0;
    --sky-low: #a9d4f2;
    --tree-green: #3f7a33;
    --grass-green: #6fb343;
    --haze-sky: #e8ecf4;
    --haze-tree: #cdd6c6;
    --haze-herd: #b9aba6;
    --haze-herd-deep: #a8958f;
    --haze-grass: #e2e6da;
    --haze-low: #f2f3ee;
  }
  * { box-sizing: border-box; margin: 0; padding: 0; }
  html, body { width: 1200px; height: 900px; overflow: hidden; }
  body {
    background: var(--backdrop);
    font-family: "Montserrat", sans-serif;
    display: flex;
    flex-direction: column;
    align-items: center;
    justify-content: center;
    gap: 40px;
  }
  .card {
    width: 640px;
    height: 366px;
    border-radius: 26px;
    overflow: hidden;
    position: relative;
    background: var(--card-white);
  }
  /* Front: contact side */
  .card-front { display: flex; }
  .contact-panel {
    width: 54%;
    padding: 40px 0 0 40px;
    display: flex;
    flex-direction: column;
  }
  .brand {
    display: flex;
    align-items: center;
    gap: 12px;
    color: var(--brand-maroon);
  }
  .brand-dot {
    width: 30px; height: 30px;
    border-radius: 50%;
    background: var(--brand-maroon);
    flex-shrink: 0;
  }
  .brand-name {
    font-weight: 700;
    font-size: 20px;
    line-height: 1.15;
    text-transform: uppercase;
    letter-spacing: 0.5px;
  }
  .person { margin-top: 40px; padding-left: 42px; }
  .person-name {
    font-size: 22px;
    font-weight: 700;
    color: var(--ink-dark);
  }
  .person-role {
    font-size: 13px;
    color: var(--ink-soft);
    margin-top: 2px;
  }
  .address {
    margin-top: 14px;
    font-size: 13px;
    color: var(--ink-soft);
    line-height: 1.35;
  }
  .contact-list {
    list-style: none;
    margin-top: 16px;
    font-size: 13px;
    color: var(--ink-soft);
  }
  .contact-list li {
    display: flex;
    align-items: center;
    gap: 10px;
    margin-bottom: 7px;
  }
  .contact-list svg { width: 13px; height: 13px; fill: var(--brand-maroon); flex-shrink: 0; }
  .pasture-photo {
    width: 46%;
    background: linear-gradient(180deg, var(--sky-top) 0%, var(--sky-low) 30%, var(--tree-green) 45%, var(--grass-green) 75%, var(--tree-green) 100%);
  }
  /* Back: logo over faded herd photo */
  .card-back {
    display: flex;
    align-items: center;
    justify-content: center;
  }
  .herd-photo {
    position: absolute;
    inset: 0;
    background: linear-gradient(180deg,
      var(--haze-sky) 0%,
      var(--haze-sky) 22%,
      var(--haze-tree) 38%,
      var(--haze-herd) 52%,
      var(--haze-herd-deep) 62%,
      var(--haze-herd) 72%,
      var(--haze-grass) 86%,
      var(--haze-low) 100%);
  }
  .brand-large { position: relative; gap: 18px; }
  .brand-large .brand-dot { width: 54px; height: 54px; }
  .brand-large .brand-name { font-size: 36px; }
</style>
</head>
<body>
  <section class="card card-front">
    <div class="contact-panel">
      <div class="brand">
        <span class="brand-dot"></span>
        <span class="brand-name">Coralbend<br>Pastoral Traders</span>
      </div>
      <div class="person">
        <p class="person-name">Daniel Harrow</p>
        <p class="person-role">Managing Director</p>
        <p class="address">27 Saddle Creek Lane<br>Bowen, QLD 4805</p>
        <ul class="contact-list">
          <li>
            <svg viewBox="0 0 24 24"><path d="M6.6 10.8a15.2 15.2 0 0 0 6.6 6.6l2.2-2.2c.3-.3.7-.4 1-.2 1.1.4 2.3.6 3.6.6.6 0 1 .4 1 1V20c0 .6-.4 1-1 1A17 17 0 0 1 3 4c0-.6.4-1 1-1h3.5c.6 0 1 .4 1 1 0 1.3.2 2.5.6 3.6.1.3 0 .7-.2 1z"/></svg>
            555.014.2287
          </li>
          <li>
            <svg viewBox="0 0 24 24"><path d="M2 5h20v14H2z M2 5l10 8 10-8" /></svg>
            info@coralbendpastoral.com
          </li>
          <li>
            <svg viewBox="0 0 24 24"><circle cx="12" cy="12" r="10"/></svg>
            www.coralbendpastoral.com
          </li>
        </ul>
      </div>
    </div>
    <div class="pasture-photo" role="img" aria-label="Photo of wagyu cattle standing in a green paddock under a blue sky"></div>
  </section>

  <section class="card card-back">
    <div class="herd-photo" role="img" aria-label="Faded photo of wagyu cattle walking through a paddock with trees and a fence behind"></div>
    <div class="brand brand-large">
      <span class="brand-dot"></span>
      <span class="brand-name">Coralbend<br>Pastoral Traders</span>
    </div>
  </section>
</body>
</html>
```